Business Cards for IT Consulting Company (Managed Service Provider)

I am looking to have some business cards printed and would like some designs. We are an IT Consulting company based in Vancouver BC. I would like a nice clean and modern look to the cards. I have uploaded all the versions of my logo so parts can be used as needed. Here is a snippit from our website homepage:

Kelbrook Systems Ltd. is an IT Solutions Partner located in Vancouver BC, Canada. We offer IT solutions and support to customers in the greater Vancouver Area. With expertise in Microsoft platforms, as well as Linux and Mac OSX and over 12 years experience in the IT industry, Kelbrook Systems is dedicated to offering our clients top quality service and products. We take pride in the solutions we offer our customers. The greatest compliment a client can give us is to recommend our services.

Kelbrook Systems Ltd. offers a wide range of IT services from onsite service to remote support and managed service solutions. This allows clients to choose the support path that best suits their company’s needs. Supporting many different sized companies from small to enterprise level over the past 12 years Kelbrook Systems has the experience and expertise needed to ensure things run smoothly. Allowing our clients to focus on doing business.

Revolutionizing the way IT services are delivered.

Kelbrook Systems is dedicated to providing our clients with IT solutions that work and grow with them for years to come. This philosophy helps save money in the long run instead of replacing equipment constantly. Far too often IT solutions are not well thought out and while possibly solving the problem at hand, require replacement due to growth or quality within a very short time frame. Kelbrook Systems takes pride in providing solutions that will last and be able to accommodate growth without the need for replacement.

Industry/Entity Type

Information Technology

Contact Information for Business Card

Kelbrook Systems Ltd.
(Employee Name)
Eml: (Employees Email Address)
Web: kelbrook.me
Ph: 604-555-0142

Font styles to use
Serif
Sans Serif

Requirements
Must have
• The Company logo and company colors.
Nice to have
• - Our tag line: "Technology Built To Last" or "Revolutionizing the way IT services are delivered."
• - Also I really like the idea of nature and technology together blending which is sort of where my logo came from so integrating that somehow onto the business cards would be great.

```html
<!DOCTYPE html>
<html lang="en">
<head>
<meta charset="utf-8">
<title>Kelbrook Systems Ltd. — Business Card</title>
<link href="https://fonts.googleapis.com/css2?family=Source+Sans+3:wght@400;600&display=swap" rel="stylesheet">
<style>
  :root {
    --stage: #3b3b3b;
    --paper: #f7f7f7;
    --brand-blue: #0aa2e0;
    --brand-blue-deep: #0896cf;
    --brand-blue-soft: #149fd6;
    --brand-grey: #55565a;
    --ink-white: #ffffff;
  }
  html, body {
    margin: 0;
    width: 1200px;
    height: 750px;
    overflow: hidden;
    background: var(--stage);
    font-family: "Source Sans 3", "Myriad Pro", sans-serif;
  }
  .stage {
    position: relative;
    width: 1200px;
    height: 750px;
  }
  .card {
    position: absolute;
    top: 228px;
    width: 461px;
    height: 263px;
    overflow: hidden;
  }
  .card--front { left: 124px; background: var(--paper); }
  .card--back  { left: 618px; background: var(--brand-blue); }

  .front-wave {
    position: absolute;
    inset: 0;
    width: 100%;
    height: 100%;
  }
  .wave-grey { fill: var(--brand-grey); }
  .wave-blue { fill: var(--brand-blue); }

  .wordmark {
    position: absolute;
    left: 34px;
    top: 76px;
    display: flex;
    align-items: center;
    gap: 8px;
    color: var(--brand-blue);
    font-weight: 600;
    font-size: 21px;
  }
  .wordmark-dot {
    width: 22px;
    height: 22px;
    border-radius: 50%;
    background: var(--brand-blue);
  }

  .contact {
    position: absolute;
    right: 27px;
    top: 113px;
    text-align: right;
    color: var(--ink-white);
  }
  .contact-name {
    margin: 0 0 9px;
    font-size: 21px;
    font-weight: 600;
    line-height: 1.1;
  }
  .contact-address {
    margin: 0 0 7px;
    font-size: 13.5px;
    line-height: 17px;
    font-style: normal;
  }
  .contact-lines {
    list-style: none;
    margin: 0;
    padding: 0;
    font-size: 13.5px;
    line-height: 17.5px;
  }
  .contact-lines li {
    display: flex;
    justify-content: flex-end;
    align-items: center;
    gap: 9px;
  }
  .contact-icon {
    width: 11px;
    height: 11px;
    fill: var(--ink-white);
  }

  .back-texture {
    position: absolute;
    inset: 0;
    background: linear-gradient(160deg, var(--brand-blue) 0%, var(--brand-blue-deep) 100%);
  }
  .back-mark {
    position: absolute;
    left: 0;
    right: 0;
    top: 118px;
    display: flex;
    align-items: center;
    justify-content: center;
    gap: 9px;
    color: var(--ink-white);
    font-weight: 600;
    font-size: 23px;
  }
  .back-mark-dot {
    width: 26px;
    height: 26px;
    border-radius: 50%;
    border: 2px solid var(--ink-white);
    box-sizing: border-box;
  }
  .tagline {
    position: absolute;
    left: 0;
    right: 0;
    top: 206px;
    margin: 0;
    text-align: center;
    color: var(--ink-white);
    font-weight: 600;
    font-size: 14px;
  }
</style>
</head>
<body>
<main class="stage">

  <section class="card card--front" aria-label="Card front">
    <svg class="front-wave" viewBox="0 0 576 328" preserveAspectRatio="none" aria-hidden="true">
      <path class="wave-grey" d="M0,228 C80,270 200,302 300,226 C390,160 440,70 576,68 L576,328 L0,328 Z"/>
      <path class="wave-blue" d="M0,255 C80,290 200,300 300,230 C390,164 440,86 576,82 L576,328 L0,328 Z"/>
    </svg>

    <div class="wordmark">
      <span class="wordmark-dot"></span>
      <span class="wordmark-name">Kelbrook Systems Ltd.</span>
    </div>

    <div class="contact">
      <h1 class="contact-name">Daniel Reyes</h1>
      <address class="contact-address">
        4812 Cedar Ridge Lane<br>
        Burnaby, BC V5G 2K9
      </address>
      <ul class="contact-lines">
        <li>604-555-0142
          <svg class="contact-icon" viewBox="0 0 24 24" aria-hidden="true"><path d="M6.6 10.8a15.2 15.2 0 0 0 6.6 6.6l2.2-2.2a1 1 0 0 1 1-.25 11.4 11.4 0 0 0 3.6.57 1 1 0 0 1 1 1V20a1 1 0 0 1-1 1A17 17 0 0 1 3 4a1 1 0 0 1 1-1h3.5a1 1 0 0 1 1 1c0 1.25.2 2.45.57 3.6a1 1 0 0 1-.25 1z"/></svg>
        </li>
        <li>dreyes@kelbrook.me
          <svg class="contact-icon" viewBox="0 0 24 24" aria-hidden="true"><path d="M2 5h20v14H2z M2 5l10 8 10-8" fill="none" stroke="#fff" stroke-width="2.4"/></svg>
        </li>
        <li>www.kelbrook.me
          <svg class="contact-icon" viewBox="0 0 24 24" aria-hidden="true"><circle cx="12" cy="12" r="10" fill="none" stroke="#fff" stroke-width="2.4"/><path d="M2 12h20M12 2c3 3 3 17 0 20M12 2c-3 3-3 17 0 20" fill="none" stroke="#fff" stroke-width="1.8"/></svg>
        </li>
      </ul>
    </div>
  </section>

  <section class="card card--back" aria-label="Card back">
    <div class="back-texture" role="img" aria-label="Faint interlocking hexagon pattern in light blue across the card back"></div>
    <div class="back-mark">
      <span class="back-mark-dot"></span>
      <span>Kelbrook Systems</span>
    </div>
    <p class="tagline">Technology Built To Last</p>
  </section>

</main>
</body>
</html>
```